Side of Page Partnership-type Letterhead Design for Chiropractic Office

Side oriented letterhead with practice locations/demographics, physician names and company logo

Target Market(s)

Healthcare Professionals & Attorneys

Industry/Entity Type

Healthcare

Font styles to use
Other font styles liked:
• Font of Logo is Trajan Pro, but not a deal breaker if we try something else

Colors

Designer to choose colors to be used in the design.

Requirements
Must have
• All info from attached documents

```html
<!DOCTYPE html>
<html lang="en">
<head>
<meta charset="utf-8">
<title>Keystone Chiropractic Letterhead</title>
<link rel="stylesheet" href="https://fonts.googleapis.com/css2?family=EB+Garamond:wght@400;600;700&display=swap">
<style>
  :root {
    --backdrop: #333333;
    --paper: #ffffff;
    --ink: #111111;
    --brand-blue: #25338a;
    --brand-orange: #f29100;
    --brand-green: #66a127;
  }
  * { box-sizing: border-box; margin: 0; padding: 0; }
  html, body {
    width: 1200px; height: 1200px; overflow: hidden;
    background: var(--backdrop);
  }
  .letterhead {
    position: absolute; left: 136px; top: 0;
    width: 928px; height: 1200px;
    background: var(--paper);
    font-family: "EB Garamond", Garamond, serif;
    color: var(--ink);
  }
  .brand {
    position: absolute; left: 71px; top: 70px;
    display: flex; align-items: center; gap: 12px;
    font-weight: 400; color: #222222; line-height: 1;
  }
  .brand-name { font-size: 40px; letter-spacing: 1px; }
  .brand-name span { display: block; font-size: 40px; }
  .brand-mark { width: 26px; height: 26px; background: var(--brand-green); }
  .physicians {
    position: absolute; left: 647px; top: 71px;
    padding-left: 13px;
    border-left: 3px solid;
    border-image: linear-gradient(var(--brand-blue) 0 33%, var(--brand-orange) 33% 66%, var(--brand-green) 66% 100%) 1;
    list-style: none; font-size: 17px; line-height: 22px;
  }
  .physicians li { white-space: nowrap; }
  .physicians strong { font-weight: 700; }
  .locations {
    position: absolute; left: 159px; top: 1035px;
    display: flex; font-size: 17px; line-height: 19px;
  }
  .location { width: 227px; }
  .location:nth-child(2) { width: 218px; }
  .location h2 {
    font-size: 17px; font-weight: 700; text-decoration: underline;
    line-height: 24px; margin-bottom: 1px;
  }
  .location--north h2 { color: var(--brand-blue); }
  .location--east h2 { color: var(--brand-orange); }
  .location--mill h2 { color: var(--brand-green); }
  .location strong { font-weight: 700; }
  .color-band {
    position: absolute; left: 0; bottom: 0; width: 100%; height: 26px;
    display: flex;
  }
  .color-band div { flex: 1; }
</style>
</head>
<body>
<main class="letterhead">
  <header class="brand">
    <div class="brand-name">KEYSTONE<span>CHIROPRACTIC</span></div>
    <div class="brand-mark"></div>
  </header>

  <ul class="physicians">
    <li><strong>Daniel Ashcroft</strong>, DC, DACNB</li>
    <li><strong>Owen Ashcroft</strong>, DC</li>
    <li><strong>Grant Whitley</strong>, DC</li>
    <li><strong>Lucas Fairbanks</strong>, DC</li>
    <li><strong>Miles Corwin</strong>, DC</li>
    <li><strong>Ethan Pellworth</strong>, DC</li>
    <li><strong>Nolan Brightman</strong>, DC</li>
  </ul>

  <footer class="locations">
    <section class="location location--north">
      <h2>Northgate</h2>
      <p>1420 N. Elm St.<br>Northgate, OH 43000<br>P: <strong>555-210-4400</strong><br>F: 555-210-4401</p>
    </section>
    <section class="location location--east">
      <h2>Eastbrook</h2>
      <p>275 S. Cedar Rd<br>Eastbrook, OH 43001<br>P: <strong>555-318-4400</strong><br>F: 555-318-4401</p>
    </section>
    <section class="location location--mill">
      <h2>Millbrook</h2>
      <p>518 N. Maple St.<br>Millbrook, OH 43002<br>P: <strong>555-427-4400</strong><br>F: 555-427-4401</p>
    </section>
  </footer>

  <div class="color-band">
    <div style="background: var(--brand-blue)"></div>
    <div style="background: var(--brand-orange)"></div>
    <div style="background: var(--brand-green)"></div>
  </div>
</main>
</body>
</html>
```